Disability Service Provider Website

We are working with VEP, which provides services and job training designed to educate, facilitate, train, and assist individuals with disabilities. They describe their clients using words like Unity and Unique.
Some sites to use for content/competitors and inspiration:
https://www.skillmora.com
https://www.pwkd.org
https://www.bellowhaven.org
https://www.openmeadow.org
https://corvelan.org
Thank you for taking the time to consider designing a website for us. We are web developers based in Stockton, CA, USA. Most of our projects go through the same process. Understanding this process may help you win a project with us. We custom-code all of our websites in-house. We don’t have any requirements as to what tools you use for your design, but we prefer Figma files. For any design that we label as four-stars, we send it to the client for review. The client picks the final design they want us to use. Once we complete this process, we will continue to show additional clients all the four-star sites and purchase them later. Your designs will have multiple chances to sell. For better chances of success, we ask that you follow these guidelines.
IMAGES:
If you use any images or icons in the design, we ask that you have a link to the asset so we can purchase the image/icon. Most of the designs we submit do not have the customer’s images on them unless they have some great images. Be creative; show us the feeling you are trying to portray with your image choices. Use any royalty-free site you choose. We subscribe to Stellic and mainly use their images, but we can purchase images outside of Stellic.
PLEASE NOTE: we will not submit designs to clients with watermarks on the images.
FONTS:
We ask that you identify the fonts used in the design. This can be done in a message if you want. We typically use Bramble Fonts and Stellic Fonts.
CONTENT:
We're always open to different content and ideas. We often submit designs with stock images so the client can see our vision. We typically take pictures after the website launch to use their images with our vision. Lorem Ipsum is fine for paragraphs, but we ask that you write the headers in correct English. We want to be able to show the vision and identify the sections of the website.
INSPIRATION:
We typically add a couple of links in the brief of websites we like to help you get started in your design.
REVISIONS:
We do not often ask for revisions of the designs unless we see something in the design that may not appeal to the client. If there are slight changes that we want to make, we do that in the development process.
FEEDBACK:
We rarely give feedback on designs during the design process. We are working on many website projects and do not have the time to provide feedback. We usually respond if your request is well thought out and asks specific questions, but a note asking “feedback, please” usually goes unanswered.
Number of Pages Required
1 page
Look and feel
Each slider illustrates characteristics of the customer's brand and the style your logo design should communicate.

```html
<!DOCTYPE html>
<html lang="en">
<head>
<meta charset="utf-8">
<title>VEP — Your Voice For Disability</title>
<link href="https://fonts.googleapis.com/css2?family=Poppins:wght@400;500;600;700;800&family=Yellowtail&display=swap" rel="stylesheet">
<style>
:root{
  --red:#8e0f18;
  --teal:#245a6e;
  --ink:#1b1b1b;
  --muted:#6d6d6d;
  --white:#ffffff;
  --line:#e7e7e7;
}
*{box-sizing:border-box;margin:0;padding:0}
html,body{width:1200px;height:3807px;overflow:hidden;background:var(--white)}
body{position:relative;font-family:"Poppins",sans-serif;color:var(--ink)}
.abs{position:absolute}
.btn{position:absolute;background:var(--teal);color:#fff;font-size:10px;font-weight:600;letter-spacing:.3px;border-radius:5px;display:flex;align-items:center;justify-content:center;text-transform:uppercase}

/* header */
.site-header{position:absolute;left:0;top:0;width:1200px;height:84px;border-bottom:2px solid var(--red);background:#fff}
.brand{position:absolute;left:110px;top:18px;font-size:34px;font-weight:700;color:var(--red);letter-spacing:1px;display:flex;align-items:center;gap:8px}
.brand-dot{width:12px;height:12px;border-radius:50%;background:var(--red)}
.nav{position:absolute;left:403px;top:30px;display:flex;gap:26px;font-size:10px;color:#444}
.nav a{color:inherit;text-decoration:none;padding:3px 7px}
.nav a.active{border:1.5px solid var(--red);border-radius:5px;color:var(--red)}
.contact-top{position:absolute;top:32px;font-size:10px;color:#444;display:flex;align-items:center;gap:10px}

/* hero */
.hero{position:absolute;left:0;top:85px;width:1200px;height:559px;background:#f4f2ef;overflow:hidden}
.hero-photo{position:absolute;left:420px;top:0;width:780px;height:559px;background:linear-gradient(160deg,#d9cdbf,#b7a38f 45%,#7b6b5f)}
.hero-fade{position:absolute;left:0;top:0;width:1200px;height:559px;background:linear-gradient(90deg,#f7f6f4 0%,rgba(247,246,244,.95) 38%,rgba(247,246,244,0) 62%)}
.hero-script{position:absolute;left:106px;top:165px;font-family:"Yellowtail",cursive;font-size:66px;color:var(--teal)}
.hero-title{position:absolute;left:104px;top:245px;font-size:71px;font-weight:800;color:var(--red);letter-spacing:1px;line-height:1}
.hero-text{position:absolute;left:106px;top:333px;width:400px;font-size:11px;line-height:16px;color:#222}

/* about */
.about-ring{position:absolute;left:95px;top:776px;width:416px;height:416px;border:4px solid var(--teal);border-radius:50%}
.about-photo{position:absolute;left:110px;top:791px;width:386px;height:386px;border-radius:50%;background:linear-gradient(150deg,#e9e3da,#c9b8a4 55%,#8c7762)}
.eyebrow{font-size:13px;font-weight:500;color:var(--teal)}
.section-title{font-size:52px;font-weight:800;color:var(--red);line-height:1}
.body-text{font-size:11px;line-height:22px;color:var(--muted)}

/* services */
.services{position:absolute;left:0;top:1313px;width:1200px;height:759px;background:linear-gradient(180deg,#a02a32,#8e0f18 70%,#7e0c14)}
.service-card{position:absolute;top:234px;width:311px;height:372px;background:#fff;border-radius:10px;text-align:center}
.service-icon{position:absolute;left:100px;top:45px;width:110px;height:110px;border-radius:50%;background:var(--teal);display:flex;align-items:center;justify-content:center}
.service-card h3{position:absolute;left:0;right:0;top:193px;font-size:20px;font-weight:500}
.service-card p{position:absolute;left:50px;right:50px;top:248px;font-size:11px;line-height:22px;color:var(--muted)}

/* news */
.news-card{position:absolute;top:2366px;width:468px;height:329px;background:#fff;border-radius:8px;box-shadow:0 6px 20px rgba(0,0,0,.08);overflow:hidden}
.news-photo{height:254px;border-bottom:2px solid var(--red)}
.news-card h3{text-align:center;font-size:20px;font-weight:500;color:var(--red);margin-top:23px}
.news-excerpt{position:absolute;top:2722px;width:468px;text-align:center;font-size:11px;line-height:23px;color:var(--muted)}
.news-meta{position:absolute;top:2791px;width:468px;display:flex;justify-content:center;gap:40px;font-size:11px;color:var(--teal)}
.news-meta span{display:flex;align-items:center;gap:6px}

/* testimonials */
.testimonial-box{position:absolute;left:111px;top:2997px;width:983px;height:286px;border:2px solid var(--teal);border-radius:22px}
.testimonial-title{position:absolute;left:385px;top:2970px;width:430px;background:#fff;text-align:center}
.avatar{position:absolute;left:219px;top:3061px;width:94px;height:94px;border-radius:50%;background:linear-gradient(160deg,#d8d8da,#9ea2a8)}

/* footer */
.site-footer{position:absolute;left:0;top:3424px;width:1200px;height:383px;background:var(--teal);color:#fff}
.site-footer .brand-foot{position:absolute;left:113px;top:74px;font-size:32px;font-weight:700;letter-spacing:1px}
.site-footer p,.site-footer li{font-size:11px;line-height:17px}
.site-footer h4{position:absolute;font-size:13px;font-weight:500}
.social{position:absolute;left:113px;top:200px;display:flex;gap:12px}
.social span{width:23px;height:23px;border:1.2px solid #fff;border-radius:50%}
.foot-links{position:absolute;list-style:none}
.foot-links li{margin-bottom:12px}
.contact-row{position:absolute;left:940px;display:flex;gap:14px;font-size:11px;line-height:20px}
</style>
</head>
<body>

<header class="site-header">
  <div class="brand"><span>VEP</span></div>
  <nav class="nav">
    <a class="active">Home</a><a>About</a><a>Services</a><a>Testimonials</a><a>News</a><a>Contact</a>
  </nav>
  <div class="contact-top" style="left:855px">
    <svg width="16" height="13" viewBox="0 0 16 13" fill="none" stroke="#8e0f18" stroke-width="1.3"><rect x="1" y="1" width="14" height="11" rx="2"/><path d="M1.5 2l6.5 5 6.5-5"/></svg>
    hello@vepcare.org
  </div>
  <div class="contact-top" style="left:998px">
    <svg width="15" height="15" viewBox="0 0 24 24" fill="none" stroke="#8e0f18" stroke-width="1.8"><path d="M22 16.9v3a2 2 0 0 1-2.2 2 19.8 19.8 0 0 1-8.6-3.1 19.5 19.5 0 0 1-6-6A19.8 19.8 0 0 1 2.1 4.2 2 2 0 0 1 4.1 2h3a2 2 0 0 1 2 1.7c.1.9.4 1.8.7 2.7a2 2 0 0 1-.5 2.1L8 9.8a16 16 0 0 0 6 6l1.3-1.3a2 2 0 0 1 2.1-.4c.9.3 1.8.6 2.7.7a2 2 0 0 1 1.7 2z"/></svg>
    +1 209 555 0147
  </div>
</header>

<section class="hero">
  <div class="hero-photo" role="img" aria-label="Photo of a smiling woman in a wheelchair reading a book with a young boy on her lap in a bright living room"></div>
  <div class="hero-fade"></div>
  <div class="hero-script">Your Voice For</div>
  <h1 class="hero-title">DISABILITY</h1>
  <p class="hero-text">We provides services and job training designed to educate, facilitate, train, and assist individuals with disabilities.</p>
  <div class="btn" style="left:106px;top:391px;width:116px;height:38px">Send Request</div>
</section>

<section class="about">
  <div class="about-ring"></div>
  <div class="about-photo" role="img" aria-label="Photo of a woman in a wheelchair reaching toward a small child at home"></div>
  <div class="abs eyebrow" style="left:632px;top:851px">Who We Are</div>
  <h2 class="abs section-title" style="left:631px;top:876px">ABOUT US</h2>
  <p class="abs body-text" style="left:632px;top:952px;width:430px">Mauris pulvinar odio id dolor sodales, non hendrerit elit porttitor. Vestibulum ante ipsum primis in faucibus orci luctus et ultrices posuere cubilia curae; Morbi suscipit, ligula non lacinia pretium, turpis libero consequat tellus, quis tempor tellus sapien sit amet neque.</p>
  <div class="btn" style="left:632px;top:1073px;width:106px;height:37px">Learn More</div>
</section>

<section class="services" role="img" aria-label="Red-tinted background photo of a person in a wheelchair">
  <div class="abs" style="left:0;right:0;top:94px;text-align:center;font-size:13px;font-weight:500;color:#fff">What We Offer</div>
  <h2 class="abs section-title" style="left:0;right:0;top:125px;text-align:center;color:#fff">OUR SERVICES</h2>

  <div class="service-card" style="left:109px">
    <div class="service-icon">
      <svg width="46" height="50" viewBox="0 0 46 50" fill="none" stroke="#fff" stroke-width="2.4" stroke-linecap="round"><path d="M9 4h10M11 4l1 18 2 24M17 4l-1 18-2 24M10 14h8M27 4h10M29 4l1 18 2 24M35 4l-1 18-2 24M28 14h8"/></svg>
    </div>
    <h3>Educate</h3>
    <p>Mauris pulvinar odio id dolor sodales, non hendrerit elit porttitor. Vestibulum</p>
  </div>
  <div class="service-card" style="left:445px">
    <div class="service-icon">
      <svg width="50" height="50" viewBox="0 0 50 50" fill="none" stroke="#fff" stroke-width="2.4" stroke-linecap="round" stroke-linejoin="round"><circle cx="18" cy="7" r="3.5"/><path d="M18 13v14h14l6 12 5-2"/><path d="M18 19h10"/><path d="M13 23a11 11 0 1 0 15 13"/></svg>
    </div>
    <h3>Facilitate</h3>
    <p>Mauris pulvinar odio id dolor sodales, non hendrerit elit porttitor. Vestibulum</p>
  </div>
  <div class="service-card" style="left:780px">
    <div class="service-icon">
      <svg width="52" height="40" viewBox="0 0 52 40" fill="none" stroke="#fff" stroke-width="2.4" stroke-linecap="round" stroke-linejoin="round"><path d="M4 24l6-16h6M48 24l-6-16h-6"/><rect x="4" y="22" width="18" height="14" rx="6"/><rect x="30" y="22" width="18" height="14" rx="6"/><path d="M22 27c2-2 6-2 8 0"/></svg>
    </div>
    <h3>Train</h3>
    <p>Mauris pulvinar odio id dolor sodales, non hendrerit elit porttitor. Vestibulum</p>
  </div>
</section>

<section class="news">
  <div class="abs eyebrow" style="left:0;right:0;top:2210px;text-align:center">From The News</div>
  <h2 class="abs section-title" style="left:0;right:0;top:2235px;text-align:center">LATEST NEWS</h2>

  <article class="news-card" style="left:109px">
    <div class="news-photo" role="img" aria-label="Photo of a young woman sitting in a wheelchair by a window in a modern living room" style="background:linear-gradient(120deg,#3d4a55,#8c8f8f 45%,#d9d4cc)"></div>
    <h3>Disability Rights</h3>
  </article>
  <p class="news-excerpt" style="left:109px">Mauris pulvinar odio id dolor sodales, non hendrerit<br>elit porttitor. Vestibulum ante ipsum primis in faucibus orci luctus et ultrices</p>
  <div class="news-meta" style="left:109px">
    <span>2 Comments</span>
    <span><svg width="16" height="16" viewBox="0 0 24 24" fill="none" stroke="#245a6e" stroke-width="1.8"><circle cx="12" cy="8" r="4"/><path d="M4 21c1-4 4.5-6 8-6s7 2 8 6"/></svg>By Marlow</span>
  </div>

  <article class="news-card" style="left:627px">
    <div class="news-photo" role="img" aria-label="Close-up photo of a hand reading braille on a page" style="background:linear-gradient(110deg,#f1efec,#e4e1dc 45%,#6a4632 70%,#3b2418)"></div>
    <h3>Changing Lives</h3>
  </article>
  <p class="news-excerpt" style="left:627px">Mauris pulvinar odio id dolor sodales, non hendrerit<br>elit porttitor. Vestibulum ante ipsum primis in faucibus orci luctus et ultrices</p>
  <div class="news-meta" style="left:627px">
    <span>2 Comments</span>
    <span><svg width="16" height="16" viewBox="0 0 24 24" fill="none" stroke="#245a6e" stroke-width="1.8"><circle cx="12" cy="8" r="4"/><path d="M4 21c1-4 4.5-6 8-6s7 2 8 6"/></svg>By Marlow</span>
  </div>
</section>

<section class="testimonials">
  <div class="testimonial-box"></div>
  <h2 class="testimonial-title section-title">TESTIMONIALS</h2>
  <div class="avatar" role="img" aria-label="Portrait photo of the client"></div>
  <div class="abs" style="left:190px;width:152px;top:3182px;text-align:center;font-size:20px;font-weight:500">R. Calder</div>
  <svg class="abs" style="left:393px;top:3088px" width="100" height="18" viewBox="0 0 100 18" fill="#245a6e">
    <g id="star"><path d="M9 1l2.4 5.2 5.6.6-4.2 3.8 1.2 5.6L9 13.4 4 16.2l1.2-5.6L1 6.8l5.6-.6z"/></g>
    <use href="#star" x="20"/><use href="#star" x="40"/><use href="#star" x="60"/><use href="#star" x="80"/>
  </svg>
  <p class="abs body-text" style="left:393px;top:3128px;width:600px">Mauris pulvinar odio id dolor sodales, non hendrerit elit porttitor. Vestibulum ante ipsum primis in faucibus orci luctus et ultrices posuere cubilia curae; Morbi suscipit, ligula non lacinia pretium, turpis libero consequat tellus, quis tempor tellus sapien sit amet neque.</p>
</section>

<footer class="site-footer">
  <div class="brand-foot">VEP</div>
  <p class="abs" style="left:113px;top:136px;width:390px">We provides services and job training designed to educate, facilitate, train, and assist individuals with disabilities.</p>
  <div class="social"><span></span><span></span><span></span><span></span></div>
  <p class="abs" style="left:113px;top:256px">Copyright © 2024 VEP. All rights reserved.</p>

  <h4 style="left:631px;top:106px">Pages</h4>
  <ul class="foot-links" style="left:631px;top:153px"><li>Home</li><li>About</li><li>Services</li><li>Testimonials</li></ul>
  <ul class="foot-links" style="left:751px;top:153px"><li>News</li><li>Contact</li></ul>

  <h4 style="left:940px;top:106px">Contact Info</h4>
  <div class="contact-row" style="top:146px">
    <svg width="15" height="18" viewBox="0 0 24 28" fill="none" stroke="#fff" stroke-width="1.8"><path d="M12 26s9-8 9-15a9 9 0 0 0-18 0c0 7 9 15 9 15z"/><circle cx="12" cy="11" r="3"/></svg>
    <span>48 Harbor Lane,<br>Lodi, CA 95240</span>
  </div>
  <div class="contact-row" style="top:204px">
    <svg width="15" height="15" viewBox="0 0 24 24" fill="none" stroke="#fff" stroke-width="1.8"><path d="M22 16.9v3a2 2 0 0 1-2.2 2 19.8 19.8 0 0 1-8.6-3.1 19.5 19.5 0 0 1-6-6A19.8 19.8 0 0 1 2.1 4.2 2 2 0 0 1 4.1 2h3a2 2 0 0 1 2 1.7c.1.9.4 1.8.7 2.7a2 2 0 0 1-.5 2.1L8 9.8a16 16 0 0 0 6 6l1.3-1.3a2 2 0 0 1 2.1-.4c.9.3 1.8.6 2.7.7a2 2 0 0 1 1.7 2z"/></svg>
    <span>(209) 555-0147</span>
  </div>
  <div class="contact-row" style="top:244px">
    <svg width="16" height="13" viewBox="0 0 16 13" fill="none" stroke="#fff" stroke-width="1.3"><rect x="1" y="1" width="14" height="11" rx="2"/><path d="M1.5 2l6.5 5 6.5-5"/></svg>
    <span>hello@vepcare.org</span>
  </div>
</footer>

</body>
</html>
```